the letter head should have the logo ( may be top left), " Larkfield Health Institute" (may be top/middle ) and the two clinics info in a vertical column ( along the left side of the page )

other physicians and official letters

• the info provided in the attachements

```html
<!DOCTYPE html>
<html lang="en">
<head>
<meta charset="utf-8">
<title>Larkfield Health Institute – Stationery</title>
<link href="https://fonts.googleapis.com/css2?family=Open+Sans:ital,wght@0,400;0,600;1,400;1,600&display=swap" rel="stylesheet">
<style>
  :root {
    --backdrop: #aaa8a8;
    --paper: #f5f4f2;
    --navy: #283845;
    --magenta: #a8256f;
    --blush: #e6b3c8;
    --text: #3a3f45;
    --white: #ffffff;
  }
  * { margin: 0; padding: 0; box-sizing: border-box; }
  html, body { width: 1200px; height: 779px; overflow: hidden; }
  body {
    background: var(--backdrop);
    font-family: "Open Sans", sans-serif;
    color: var(--text);
    position: relative;
  }
  .sheet {
    position: absolute;
    background: var(--paper);
    box-shadow: 2px 3px 6px rgba(0,0,0,.25);
    overflow: hidden;
  }
  .edge-band { position: absolute; left: 0; width: 8px; }
  .edge-band.navy { background: var(--navy); }
  .edge-band.magenta { background: var(--magenta); }
  .edge-band.blush { background: var(--blush); }

  .brand { position: absolute; display: flex; align-items: center; gap: 8px; }
  .brand-square { width: 44px; height: 44px; background: var(--navy); flex: none; }
  .brand-name {
    font-family: "Open Sans", sans-serif;
    font-weight: 600;
    font-size: 13px;
    color: var(--navy);
    white-space: nowrap;
  }

  .office { position: absolute; font-size: 9.6px; line-height: 12.4px; }
  .office-title { font-weight: 600; color: var(--navy); }
  .office b { font-weight: 600; color: var(--navy); }
  .dotted { border-top: 1px dotted var(--text); width: 102px; margin: 2px 0; }
  .rule { border-top: 1px solid var(--text); width: 105px; margin: 6px 0 9px; }

  .mark { position: absolute; text-align: center; }
  .mark-square { background: var(--navy); margin: 0 auto; }
  .web { font-size: 9.6px; font-style: italic; color: var(--text); white-space: nowrap; }

  .letterhead { left: 37px; top: 33px; width: 506px; height: 713px; }
  .envelope-back { left: 587px; top: 184px; width: 567px; height: 258px; }
  .flap { position: absolute; left: 0; top: 0; width: 567px; height: 96px; }
  .flap-content {
    position: absolute; left: 0; right: 0; top: 11px; text-align: center; color: var(--white);
  }
  .flap-square { width: 46px; height: 56px; background: var(--white); margin: 0 auto; }
  .flap-web { font-size: 9px; font-style: italic; font-weight: 600; margin-top: 8px; }
  .envelope-front { left: 585px; top: 486px; width: 568px; height: 259px; }
</style>
</head>
<body>

<section class="sheet letterhead">
  <div class="edge-band navy" style="top:0;height:236px"></div>
  <div class="edge-band magenta" style="top:238px;height:237px"></div>
  <div class="edge-band blush" style="top:477px;height:236px"></div>

  <div class="brand" style="left:38px;top:34px">
    <div class="brand-square"></div>
    <div class="brand-name">Larkfield Health Institute</div>
  </div>

  <div class="office" style="left:33px;top:551px">
    <div class="office-title">Westbrook Office</div>
    <div>2275 N. Alder Rd.</div>
    <div>Westbrook 71620</div>
    <div class="dotted"></div>
    <div><b>P :</b> 870-555-0142</div>
    <div><b>F :</b> 870-555-0143</div>
    <div class="rule"></div>
    <div class="office-title">Hollis Park office</div>
    <div>612 E. Ridgeway Ave.</div>
    <div>Suite 210, 72231</div>
    <div class="dotted"></div>
    <div><b>P :</b> 501-555-0186</div>
    <div><b>F :</b> 501-555-0187</div>
  </div>

  <div class="mark" style="left:376px;top:602px;width:110px">
    <div class="mark-square" style="width:58px;height:72px"></div>
    <div class="web" style="margin-top:10px">www.larkfieldhealth.com</div>
  </div>
</section>

<section class="sheet envelope-back">
  <svg class="flap" viewBox="0 0 567 96" aria-hidden="true">
    <path d="M0 0 H567 L556 70 Q552 92 530 93 H37 Q15 92 11 70 Z" fill="#283845"/>
  </svg>
  <div class="flap-content">
    <div class="flap-square"></div>
    <div class="flap-web">www.larkfieldhealth.com</div>
  </div>
</section>

<section class="sheet envelope-front">
  <div class="edge-band navy" style="top:0;height:86px"></div>
  <div class="edge-band magenta" style="top:88px;height:85px"></div>
  <div class="edge-band blush" style="top:175px;height:84px"></div>

  <div class="brand" style="left:27px;top:22px">
    <div class="brand-square"></div>
    <div class="brand-name">Larkfield Health Institute</div>
  </div>

  <div class="office" style="left:24px;top:166px">
    <div class="office-title">Westbrook Office</div>
    <div>2275 N. Alder Rd.</div>
    <div>Westbrook 71620</div>
    <div style="height:6px"></div>
    <div class="office-title">Hollis Park office</div>
    <div>612 E. Ridgeway Ave.</div>
    <div>Suite 210, 72231</div>
  </div>

  <div class="mark" style="left:488px;top:164px;width:54px">
    <div class="mark-square" style="width:54px;height:74px"></div>
  </div>
</section>

</body>
</html>
```